Book Cover Design Project

Hello,

I am looking to get a cover created for my book.

Size 6 X 9

Title:
Quiet Ledger Steady Harvest

Sub-Title:
Plain Methods for Growing Steady Harvests From Your Quiet Ledger

Author:
Marcus Pendleby

The book could have an image or only typography.

If it does include an image do not use an image of a real person. If you use a person, he can be shaded in, outlined, etc

I like the color white and blue however, I am open to other colors as well.

Below is the cover of my previous book that has an image:
http://www.torvelbooks.example/Quiet-Harbor-Path-Found-Lasting/dp/284710362Q/ref=sr_1_1?ie=UTF8&s=books&qid=2417307529&sr=1-1

I like simple designs but open to other concepts also

attached is the text to be used for the back of the book.

Thank you in advance for your designs,

Target Market(s)

This book will be for small business owners. Typically males/females between the age of 25 - 45 looking to make more money without going broke with marketing.

Industry/Entity Type

Business

Requirements
Must have
• Must include the Title, Subtitle and Author on the cover

Nice to have
• An image that represents a small business growing
Should not have
• Images of a real person. Stylized versions are ok.

```html
<!DOCTYPE html>
<html lang="en">
<head>
<meta charset="utf-8">
<title>Quiet Ledger Steady Harvest — Cover Spread</title>
<link rel="stylesheet" href="https://fonts.googleapis.com/css2?family=PT+Sans:wght@400;700&family=PT+Sans+Narrow:wght@700&family=PT+Serif&display=swap">
<style>
  :root {
    --page-bg: #e3e4e6;
    --paper: #ffffff;
    --brand-blue: #0f4f9c;
    --link-blue: #1a5fb0;
    --ink: #1f1f1f;
    --spine-shade: #e9eaec;
    --art-light: #eef2fb;
    --art-mid: #a9bff0;
  }
  * { margin: 0; padding: 0; box-sizing: border-box; }
  html, body { width: 1200px; height: 882px; overflow: hidden; }
  body { background: var(--page-bg); font-family: "PT Sans", sans-serif; color: var(--ink); }

  .spread {
    position: absolute; left: 27px; top: 22px; width: 1146px; height: 838px;
    background: var(--paper);
    box-shadow: 0 1px 6px rgba(0,0,0,.25);
  }

  /* Back cover */
  .back-cover { position: absolute; left: 0; top: 0; width: 546px; height: 100%; }
  .back-headline {
    position: absolute; left: 34px; top: 24px; width: 420px;
    font-weight: 700; font-size: 24px; line-height: 34px; color: var(--brand-blue);
    text-indent: -11px; padding-left: 11px;
  }
  .back-body {
    position: absolute; left: 49px; top: 180px; width: 432px;
    font-size: 15.4px; line-height: 20.8px;
  }
  .back-body p { margin-bottom: 20px; }
  .back-body .lead-in { padding-left: 4px; }
  .benefit-list { list-style: none; color: var(--link-blue); margin-bottom: 20px; }
  .benefit-list li::before { content: "• "; }
  .about-author {
    position: absolute; left: 49px; top: 652px; width: 360px;
    font-size: 12.6px; line-height: 19.5px;
  }
  .about-author h3 { font-size: 12.6px; font-weight: 700; }
  .author-site { position: absolute; left: 49px; top: 777px; font-size: 12.6px; line-height: 19.5px; }
  .author-site a { color: var(--link-blue); }

  /* Spine */
  .spine {
    position: absolute; left: 546px; top: 0; width: 64px; height: 100%;
    background: linear-gradient(90deg, var(--paper) 0%, var(--spine-shade) 45%, #dcdde0 55%, var(--paper) 100%);
  }
  .spine-author, .spine-title {
    position: absolute; left: 50%; white-space: nowrap;
    transform-origin: left top; transform: rotate(90deg);
  }
  .spine-author { top: 32px; margin-left: 8px; font-family: "PT Serif", serif; font-size: 12px; }
  .spine-title { top: 300px; margin-left: 10px; font-size: 16px; letter-spacing: .5px; color: var(--brand-blue); }
  .spine-title strong { font-weight: 700; }

  /* Front cover */
  .front-cover { position: absolute; left: 610px; top: 0; width: 536px; height: 100%; text-align: center; }
  .cover-art { position: absolute; left: 110px; top: 6px; width: 380px; height: 470px; }
  .cover-title { font-weight: 700; }
  .title-upper, .title-lower {
    position: absolute; left: 0; width: 100%; display: block; white-space: nowrap;
    font-family: "PT Sans Narrow", sans-serif; font-weight: 700; color: var(--brand-blue);
  }
  .title-upper { top: 495px; font-size: 52px; line-height: 50px; letter-spacing: .5px; }
  .title-lower { top: 554px; font-size: 80px; line-height: 90px; }
  .subtitle {
    position: absolute; left: 0; width: 100%; top: 650px;
    font-weight: 700; font-size: 17.5px; line-height: 26px;
  }
  .front-author {
    position: absolute; left: 0; width: 100%; top: 722px;
    font-family: "PT Serif", serif; font-size: 26px; color: var(--brand-blue);
  }
  .copyright-note { position: absolute; left: 0; width: 100%; top: 792px; font-size: 11px; font-weight: 700; }
</style>
</head>
<body>
<main class="spread">
  <section class="back-cover">
    <h2 class="back-headline">“Dramatically Increase Your Sales And Revenue With Effective Marketing Strategies, Guaranteed To Get Results!"</h2>
    <div class="back-body">
      <p>Are lackluster sales getting you down?</p>
      <p>Does it seem like — no matter how much testing and tweaking you do — you continue to struggle with getting new customers, creating a strong online and offline presence, and maximizing the lifetime value of existing customers, and now you're running out of time, patience… and money?</p>
      <p class="lead-in">What if I told you that I could help you:</p>
      <ul class="benefit-list">
        <li>Gain and retain new customers</li>
        <li>Get others to promote your business</li>
        <li>Make more money from your existing customers</li>
        <li>Get results that will blow your competition away</li>
      </ul>
      <p>… And I can show you how to do it FASTER, for a small fraction of what you'd pay in-house marketing employees to get the SAME results!</p>
      <p>Curious? Then open this book right now and I'll explain how it's done…</p>
    </div>
    <div class="about-author">
      <h3>About the Author:</h3>
      <p>Marcus Pendleby is a partner of Brightwell Outreach, which helps small businesses get more customers by making them findable on the Internet. He is a best selling author and has a bachelor's degree in Internet Marketing. He dedicates his time to learning as much as possible, both in marketing and in life.</p>
    </div>
    <p class="author-site">See how he can serve your business by going to<br><a href="#">www.brightwelloutreach.example</a></p>
  </section>

  <aside class="spine">
    <span class="spine-author">by Marcus Pendleby</span>
    <span class="spine-title">QUIET LEDGER <strong>STEADY HARVEST</strong></span>
  </aside>

  <section class="front-cover">
    <svg class="cover-art" viewBox="0 0 380 470" role="img" aria-label="Stylized blue 3D figure in a cap watering small dollar-sign seedlings with a watering can">
      <defs>
        <radialGradient id="artGlow" cx="55%" cy="50%" r="60%">
          <stop offset="0%" stop-color="var(--art-mid)"/>
          <stop offset="60%" stop-color="var(--art-light)"/>
          <stop offset="100%" stop-color="#ffffff"/>
        </radialGradient>
      </defs>
      <rect width="380" height="470" fill="url(#artGlow)"/>
    </svg>
    <h1 class="cover-title">
      <span class="title-upper">QUIET LEDGER</span>
      <span class="title-lower">STEADY HARVEST</span>
    </h1>
    <p class="subtitle">Plain Methods for Growing Steady Harvests<br>From Your Quiet Ledger</p>
    <p class="front-author">by Marcus Pendleby</p>
    <p class="copyright-note">Copyrighted Material</p>
  </section>
</main>
</body>
</html>
```